Parks Dept. Ad for Outside Exercise

We need a design for a 1/3 page ad in a regional fitness magazine. I got the initial design from one of our staffers at the parks dept. and knew we should/could find someone, and spend a little money to do better. I've uploaded the initial design to help with understanding the idea of what we're looking for, but feel free to go in a different direction. Obviously, less text! And I don't know why it has it twice...

Target Market(s)

people interested in fitness magazines

Industry/Entity Type

Fitness

Requirements
Must have
• must provide a sense of why outdoor exercise is desirable and that the city of Cedar Ridge provides those benefits with our wonderful park system. Logo of the city (White or blue) and Parks and Rec contact info must be in ad, though certainly not as prominent as they had displayed in the initial ad.

```html
<!DOCTYPE html>
<html lang="en">
<head>
<meta charset="utf-8">
<title>Benefits of Exercising in Nature – Cedar Ridge Parks and Recreation</title>
<link rel="stylesheet" href="https://fonts.googleapis.com/css2?family=Playball&family=PT+Sans:wght@400;700&family=PT+Serif:wght@700&display=swap">
<style>
  :root {
    --backdrop: #d6d6d6;
    --parchment-light: #efe4cf;
    --parchment-mid: #e0cfb0;
    --parchment-dark: #c2a57c;
    --ink: #35261b;
    --brand-blue: #2c3b8f;
    --band: #3b3583;
    --band-text: #ffffff;
    --sky: #a9c6e6;
    --sun: #f6d7a0;
    --trail: #b8743d;
    --brush: #8a6a2c;
  }
  * { box-sizing: border-box; margin: 0; padding: 0; }
  html, body { width: 1200px; height: 1200px; overflow: hidden; }
  body { background: var(--backdrop); position: relative; font-family: "PT Sans", Arial, sans-serif; }

  .ad {
    position: absolute; left: 120px; top: 120px;
    width: 960px; height: 960px; overflow: hidden;
  }
  .ad__photo {
    position: absolute; inset: 0;
    background:
      radial-gradient(circle at 52% 42%, var(--sun) 0%, rgba(246,215,160,0) 32%),
      linear-gradient(180deg, var(--sky) 0%, #d9c6a4 40%, var(--brush) 62%, var(--trail) 80%, #7a4a24 100%);
  }
  .ad__panel { position: absolute; inset: 0; }

  .headline { position: absolute; left: 40px; top: 42px; width: 480px; color: var(--ink); text-align: center; }
  .headline__script { font-family: "Playball", cursive; font-size: 74px; line-height: 1; }
  .headline__small { font-size: 50px; font-weight: 400; }
  .headline__big { display: block; font-weight: 700; font-size: 66px; line-height: 1.05; letter-spacing: 0.5px; }
  .headline__line { display: block; font-size: 66px; line-height: 1.05; }
  .headline__line strong { font-weight: 700; }

  .benefits { position: absolute; left: 58px; top: 278px; width: 420px; list-style: none; color: var(--ink); font-size: 24px; line-height: 1.15; }
  .benefits li { position: relative; padding-left: 16px; margin-bottom: 8px; }
  .benefits li::before { content: "•"; position: absolute; left: 0; }

  .org { position: absolute; left: 40px; top: 650px; width: 420px; text-align: center; color: var(--brand-blue); }
  .org__mark { width: 96px; height: 96px; margin: 0 auto 28px; border-radius: 50%; background: var(--brand-blue); }
  .org__name { font-family: "PT Serif", Georgia, serif; font-weight: 700; font-size: 36px; line-height: 1.1; }
  .org__dept { font-family: "PT Serif", Georgia, serif; font-weight: 700; font-size: 24px; }

  .contact {
    position: absolute; left: 0; top: 862px; width: 430px; height: 98px;
    background: var(--band); color: var(--band-text);
    font-size: 24px; line-height: 1.35; text-align: center;
    display: flex; flex-direction: column; justify-content: center;
  }
</style>
</head>
<body>
  <div class="ad">
    <div class="ad__photo" role="img" aria-label="Photo of a young man and a young woman running along a sunlit dirt trail through shrubs"></div>

    <svg class="ad__panel" viewBox="0 0 960 960" aria-hidden="true">
      <defs>
        <linearGradient id="parchment" x1="0" y1="0" x2="1" y2="1">
          <stop offset="0" stop-color="var(--parchment-light)"/>
          <stop offset="0.55" stop-color="var(--parchment-mid)"/>
          <stop offset="1" stop-color="var(--parchment-dark)"/>
        </linearGradient>
      </defs>
      <path fill="url(#parchment)" d="M0 0 H548 L552 40 L544 90 L556 150 L548 210 L540 270 L528 330 L520 380 L514 440 L508 500 L492 560 L478 620 L470 680 L452 740 L440 800 L432 862 L430 960 H0 Z"/>
    </svg>

    <h1 class="headline">
      <span class="headline__script">Benefits</span> <span class="headline__small">of</span>
      <span class="headline__big">EXERCISING</span>
      <span class="headline__line">in <strong>NATURE</strong></span>
    </h1>

    <ul class="benefits">
      <li>Improves concentration</li>
      <li>Positive affects on blood pressure and cholesterol</li>
      <li>Reduces stress</li>
      <li>Increases Vitamin D levels and helps optimize hormones</li>
      <li>Fresh air has more oxygen</li>
    </ul>

    <div class="org">
      <div class="org__mark"></div>
      <div class="org__name">Cedar Ridge</div>
      <div class="org__dept">Parks and Recreation</div>
    </div>

    <div class="contact">
      <span>crpr.org • 501-555-0142</span>
      <span>parksandrec@cedarridge.gov</span>
    </div>
  </div>
</body>
</html>
```